Business Card Re-Design/Update

We'd like to update out business cards. I've included our current "Style guide" which has the colour scheme of the organisation in it. I've also included the branding files with logos etc in them.

I've also included a copy of one of our existing cards so that you can see how ugly/dated they look. I'd like a fresh modern corporate look.

Target Market(s)

These are for our clients, potential clients, industry contacts - like all business cards

Contact Information for Business Card

Name
Position
Company Address - Level 1, 47 Garnet Lane, Toowong Qld 4066
Direct Phone
mobile
Email
Website -www.korvalnet.com.au
Logo

Colors

Designer to choose colors to be used in the design.

Requirements
Must have
• Main Logo
• Cards will need to be editable to be able to personalize them for each new employee.
Nice to have
• The MapOUT, HandOVER, UpKEEP would be okay to have if they can be sensibly and professionally added to the look without detracting from the main imagery.
• Maybe they could go on the back of the card? will leave this to your creative discretion as to whether/where they fit.
Should not have
• Should not have decorative or script fonts

```html
<!DOCTYPE html>
<html lang="en">
<head>
<meta charset="utf-8">
<title>korvalNET business card</title>
<link rel="stylesheet" href="https://fonts.googleapis.com/css2?family=Arimo:wght@400;700&display=swap">
<style>
  :root {
    --charcoal: #3d3d3f;
    --red: #d71f26;
    --orange: #e2583a;
    --white: #ffffff;
    --ink: #1c1c1c;
    --stage: #ecebe8;
    --green: #5aa72e;
    --blue: #2b8fd6;
    --magenta: #c02a97;
  }
  html, body { margin: 0; height: 100%; overflow: hidden; }
  body {
    width: 1200px; height: 1200px; background: var(--stage);
    font-family: "Arimo", Arial, sans-serif;
    display: flex; flex-direction: column; align-items: center; justify-content: center; gap: 60px;
  }
  .card {
    position: relative; width: 900px; height: 514px; background: var(--white);
    overflow: hidden; box-shadow: 0 6px 20px rgba(0,0,0,.18);
  }
  .card svg.shapes { position: absolute; inset: 0; }
  .person { position: absolute; left: 56px; top: 62px; color: var(--white); }
  .person-name { font-size: 46px; font-weight: 700; margin: 0; letter-spacing: .5px; }
  .person-name .surname { color: var(--red); }
  .person-role { font-size: 22px; margin: 6px 0 0; }
  .contact-block { position: absolute; left: 200px; top: 240px; width: 420px; }
  .contact-row { display: flex; height: 80px; align-items: center; color: var(--white); font-size: 21px; white-space: nowrap; }
  .contact-row:nth-child(odd) { background: var(--red); }
  .contact-row:nth-child(even) { background: var(--orange); }
  .contact-icon {
    width: 76px; height: 100%; background: var(--charcoal); flex: none;
    display: flex; align-items: center; justify-content: center; margin-right: 22px;
  }
  .contact-row:nth-child(even) .contact-icon { background: #5a5a5c; }
  .brand { position: absolute; display: flex; align-items: center; gap: 10px; font-weight: 700; color: var(--red); white-space: nowrap; }
  .brand-mark { background: var(--red); flex: none; }
  .brand-small { right: 48px; top: 170px; font-size: 32px; }
  .brand-small .brand-mark { width: 22px; height: 22px; }
  .company-info { position: absolute; left: 645px; top: 258px; width: 235px; font-size: 16px; color: var(--ink); line-height: 1.35; }
  .company-info .line { display: flex; gap: 10px; align-items: flex-start; margin-bottom: 14px; white-space: nowrap; }
  .company-info svg { flex: none; }
  .logo-panel {
    position: absolute; left: 110px; top: 88px; width: 470px; height: 200px; background: var(--white);
    display: flex; align-items: center; justify-content: center;
  }
  .brand-large { position: static; font-size: 68px; gap: 16px; }
  .brand-large .brand-mark { width: 44px; height: 44px; }
  .service-list { position: absolute; left: 350px; right: 36px; bottom: 44px; display: flex; justify-content: space-between; }
  .service { display: flex; align-items: center; gap: 8px; font-size: 30px; white-space: nowrap; }
  .service .dot { width: 20px; height: 20px; flex: none; }
  .service.map { color: var(--green); } .service.map .dot { background: var(--green); }
  .service.hand { color: var(--blue); } .service.hand .dot { background: var(--blue); }
  .service.keep { color: var(--magenta); } .service.keep .dot { background: var(--magenta); }
</style>
</head>
<body>

<section class="card card-front" aria-label="Card front">
  <svg class="shapes" width="900" height="514" viewBox="0 0 900 514">
    <path d="M0 0 H780 C610 50 500 140 440 270 C390 380 280 470 110 514 H0 Z" fill="var(--charcoal)"/>
    <path d="M800 0 C630 55 525 150 466 280 C415 390 305 478 150 514" fill="none" stroke="var(--red)" stroke-width="10"/>
    <rect x="690" y="0" width="34" height="22" fill="var(--red)"/>
    <rect x="730" y="0" width="34" height="22" fill="var(--orange)"/>
  </svg>

  <div class="person">
    <h1 class="person-name">Mara <span class="surname">Whitfield</span></h1>
    <p class="person-role">Business Development Manager</p>
  </div>

  <div class="brand brand-small"><span class="brand-mark"></span>korvalNET</div>

  <div class="contact-block">
    <div class="contact-row">
      <div class="contact-icon">
        <svg width="40" height="30" viewBox="0 0 40 30"><rect x="2" y="2" width="36" height="26" fill="none" stroke="#fff" stroke-width="3"/><path d="M2 2 L20 17 L38 2 M2 28 L15 14 M38 28 L25 14" fill="none" stroke="#fff" stroke-width="3"/></svg>
      </div>
      mwhitfield@korvalnet.com.au
    </div>
    <div class="contact-row">
      <div class="contact-icon">
        <svg width="26" height="40" viewBox="0 0 26 40"><rect x="2" y="2" width="22" height="36" rx="4" fill="none" stroke="#fff" stroke-width="3"/><circle cx="13" cy="32" r="2.5" fill="#fff"/></svg>
      </div>
      +61 (0)412 555 019
    </div>
    <div class="contact-row">
      <div class="contact-icon">
        <svg width="40" height="36" viewBox="0 0 40 36"><path d="M4 12 C4 4 36 4 36 12 L30 14 L28 9 H12 L10 14 Z" fill="#fff"/><rect x="8" y="16" width="24" height="18" rx="3" fill="#fff"/><g fill="var(--charcoal)"><rect x="13" y="20" width="4" height="3"/><rect x="18" y="20" width="4" height="3"/><rect x="23" y="20" width="4" height="3"/><rect x="13" y="26" width="4" height="3"/><rect x="18" y="26" width="4" height="3"/><rect x="23" y="26" width="4" height="3"/></g></svg>
      </div>
      +61 (0)7 3555 0142
    </div>
  </div>

  <div class="company-info">
    <div class="line">
      <svg width="22" height="22" viewBox="0 0 22 22"><circle cx="11" cy="11" r="9.5" fill="none" stroke="var(--ink)" stroke-width="2"/><ellipse cx="11" cy="11" rx="4" ry="9.5" fill="none" stroke="var(--ink)" stroke-width="1.6"/><path d="M1.5 11 H20.5 M3.5 6 H18.5 M3.5 16 H18.5" stroke="var(--ink)" stroke-width="1.6"/></svg>
      <span>www.korvalnet.com.au</span>
    </div>
    <div class="line">
      <svg width="22" height="22" viewBox="0 0 22 22"><path d="M11 2 L21 11 H18 V20 H4 V11 H1 Z" fill="var(--ink)"/><rect x="9" y="14" width="4" height="6" fill="#fff"/></svg>
      <span>Level 1, 47 Garnet Lane,<br>Toowong Qld 4066</span>
    </div>
  </div>
</section>

<section class="card card-back" aria-label="Card back">
  <svg class="shapes" width="900" height="514" viewBox="0 0 900 514">
    <path d="M0 0 H720 C580 50 500 170 440 270 C380 370 300 460 170 514 H0 Z" fill="var(--charcoal)"/>
    <path d="M745 0 C605 55 525 175 466 278 C408 378 330 465 210 514" fill="none" stroke="var(--red)" stroke-width="10"/>
  </svg>

  <div class="logo-panel">
    <div class="brand brand-large"><span class="brand-mark"></span>korvalNET</div>
  </div>

  <div class="service-list">
    <div class="service map"><span class="dot"></span>MapOUT</div>
    <div class="service hand"><span class="dot"></span>HandOVER</div>
    <div class="service keep"><span class="dot"></span>UpKEEP</div>
  </div>
</section>

</body>
</html>
```